I'm looking to get the bottom (underneath the window) of the attached ticket booth wrapped with a modern design. The Dimensions of the final print is 68.5" wide x 37.5" tall, plus applicable safety margins. I'm open for pretty much any idea.

Key words are:

1.) "CAPTURE YOUR EXPERIENCE WITH A MEMORABLE PHOTO"

Follow us at:
IG: @skymorrow_
FB: @my.skyMORROW

2.) Our slogan should be mentioned as well "The GRANDEST ROTOR Journey" and "Leap INTO Bold Horizons"

3.) Also, a mention of "COLD DRINKS" as well, since we sell cold beverages during each event too.

Not all of the attached pictures have to be used. I just wanted to provide as many as possible for you guys to choose from. I have attached 3 pictures of the ticket booth as well, so you get an idea of how the space underneath the window is going to look.

Target Market(s)

Aviation, General Public, Adventure

Industry/Entity Type

Aviation

Colors
0054AA
0677BA
7BADD7
CADEEF
E8F1F8

Requirements
Must have
• Our Slogan, and the 3 key facts referenced in the project description

```html
<!DOCTYPE html>
<html lang="en">
<head>
<meta charset="utf-8">
<title>skyMORROW Booth Wrap</title>
<link rel="stylesheet" href="https://fonts.googleapis.com/css2?family=Bebas+Neue&family=Open+Sans:wght@600;700&display=swap">
<style>
  :root {
    --deep-blue: #0054AA;
    --mid-blue: #0677BA;
    --sky-blue: #7BADD7;
    --pale-blue: #CADEEF;
    --mist-blue: #E8F1F8;
    --headline-blue: #1354A8;
    --night: #16233a;
    --stage: #2c2c2c;
    --white: #ffffff;
  }
  * { margin: 0; padding: 0; box-sizing: border-box; }
  html, body { width: 832px; height: 1200px; overflow: hidden; }
  body {
    background: var(--stage);
    display: flex;
    align-items: center;
    justify-content: center;
  }
  .wrap-panel {
    position: relative;
    width: 754px;
    height: 412px;
    background: var(--white);
    overflow: hidden;
  }
  .pilot-photo {
    position: absolute;
    inset: 0;
    width: 100%;
    height: 100%;
  }
  .brand {
    position: absolute;
    left: 20px;
    top: 30px;
    display: flex;
    align-items: center;
    gap: 7px;
    font-family: "Open Sans", sans-serif;
    font-weight: 600;
    font-size: 13px;
    letter-spacing: 0.5px;
    color: var(--mid-blue);
  }
  .brand-dot {
    width: 24px;
    height: 24px;
    border-radius: 50%;
    background: var(--mid-blue);
  }
  .headline {
    position: absolute;
    left: 0;
    top: 80px;
    width: 490px;
    text-align: center;
    font-family: "Bebas Neue", sans-serif;
    font-weight: 400;
    color: var(--headline-blue);
    line-height: 1;
  }
  .headline-top { display: block; font-size: 56px; }
  .headline-mid { display: block; font-size: 62px; margin-top: 2px; }
  .headline-big { display: block; font-size: 80px; margin-top: 0; }
  .tagline {
    position: absolute;
    left: 0;
    top: 290px;
    width: 490px;
    text-align: center;
    font-family: "Open Sans", sans-serif;
    font-weight: 700;
    font-size: 14px;
    letter-spacing: 0.4px;
    color: var(--mid-blue);
  }
  .band-note {
    position: absolute;
    left: 25px;
    bottom: 46px;
    font-family: "Open Sans", sans-serif;
    font-weight: 700;
    font-size: 10px;
    letter-spacing: 0.3px;
    color: var(--mist-blue);
  }
  .band-text {
    position: absolute;
    left: 25px;
    bottom: 16px;
    font-family: "Open Sans", sans-serif;
    font-weight: 700;
    font-size: 19px;
    color: var(--white);
    letter-spacing: 0.2px;
  }
  .social-pill {
    position: absolute;
    left: 523px;
    bottom: 19px;
    width: 202px;
    height: 18px;
    border-radius: 9px;
    background: var(--white);
    display: flex;
    align-items: center;
    justify-content: space-around;
    font-family: "Open Sans", sans-serif;
    font-weight: 700;
    font-size: 8px;
    color: var(--night);
  }
  .social-item { display: flex; align-items: center; gap: 3px; }
  .social-dot {
    width: 10px; height: 10px;
    border-radius: 50%;
    border: 1.2px solid var(--night);
  }
  .social-divider { width: 1px; height: 12px; background: var(--night); }
</style>
</head>
<body>
  <div class="wrap-panel">
    <svg class="pilot-photo" viewBox="0 0 754 412" role="img" aria-label="Photo of a smiling pilot with sunglasses and headset flying a helicopter, cockpit and sky behind him">
      <defs>
        <linearGradient id="skyFade" x1="0" y1="0" x2="1" y2="0">
          <stop offset="0.45" stop-color="#ffffff"/>
          <stop offset="0.65" stop-color="#E8F1F8"/>
          <stop offset="0.85" stop-color="#CADEEF"/>
          <stop offset="1" stop-color="#b9cbd8"/>
        </linearGradient>
        <radialGradient id="pilotShade" cx="0.92" cy="0.95" r="0.45">
          <stop offset="0" stop-color="#16233a"/>
          <stop offset="0.55" stop-color="#2f4260" stop-opacity="0.8"/>
          <stop offset="1" stop-color="#7BADD7" stop-opacity="0"/>
        </radialGradient>
      </defs>
      <rect width="754" height="412" fill="url(#skyFade)"/>
      <rect width="754" height="412" fill="url(#pilotShade)"/>
      <polygon points="0,335 516,354 493,412 0,412" fill="var(--mid-blue)"/>
    </svg>

    <div class="brand"><span class="brand-dot"></span>SKYMORROW.COM</div>

    <h1 class="headline">
      <span class="headline-top">The</span>
      <span class="headline-mid">GRANDEST ROTOR</span>
      <span class="headline-big">Journey</span>
    </h1>

    <p class="tagline">Leap INTO Bold Horizons</p>

    <p class="band-note">COLD DRINKS · CAPTURE YOUR EXPERIENCE WITH A MEMORABLE PHOTO</p>
    <p class="band-text">AVAIL BEVERAGE SERVICE ON BOARD</p>

    <div class="social-pill">
      <span class="social-item"><span class="social-dot"></span>: @my.skyMORROW</span>
      <span class="social-divider"></span>
      <span class="social-item"><span class="social-dot"></span>: @skymorrow_</span>
    </div>
  </div>
</body>
</html>
```